Inspiring Poster for Company Staff Room

What we need:
We want an awesome design to create a poster that will be plaque mounted in our staff room. We just went through a very motivating workshop to discover our "WHY" as a company...basically, to define the reason we are in business, and to define what motivates us to come to work every day. The poster must be motivating but really resonate with our team…we are not looking for a “typical” motivational poster that we can purchase off Amazon!

Who we are:
We are a property management company, a team of 20 that is passionate about our investors, and residents who rent from us, but more importantly, we love helping people and making a difference in our industry. We are proud and work hard for every single 5 star Google review we achieve.

Information for you:
We have included a mock up of the poster, which words we want, and the placement of them (in a general sense) but we need a designer to really bring this together in an inspiring poster that represents our company’s culture, feel, and fit. We have also included a logo file, as well as examples of our business cards, letterhead and thank you card already designed.
Here are the parameters:

(1) Poster size: 24” x 36”
(2) Full colour
(3) Must incorporate our company logo
(4) Must incorporate the following words:

Why do I come to work?

“To feel fulfilled by empathizing, educating and empowering our clients and co-workers so that we can build strong, impactful relationships”

Own the outcome

(5) Please see our website at www.brindlecovepm.com to get a feel for our company culture and for a better idea of our current company graphics

Target Market(s)

Our staff. Will not be seen by our clients

Industry/Entity Type

Real Estate

Font styles to use
Serif
Sans Serif

Requirements
Should not have
• Would not want this to be too "busy." if you can picture it, the poster will be mounted on the wall as soon as someone enters the room. The idea is to remind them each day why they come to work.

```html
<!DOCTYPE html>
<html lang="en">
<head>
<meta charset="utf-8">
<title>Why Do I Come To Work? – Brindle Cove Property Management</title>
<link rel="stylesheet" href="https://fonts.googleapis.com/css2?family=League+Spartan:wght@500;700;800;900&family=Oswald:wght@400&display=swap">
<style>
  :root {
    --ink: #141414;
    --paper: #ffffff;
    --fog: #f3f3f3;
    --fog-mid: #c9cbc6;
    --pine: #34412f;
    --pine-deep: #1f2a1c;
    --rust: #7a4a35;
    --brand-blue: #1e86c8;
    --brand-navy: #2b3a4a;
  }
  * { margin: 0; padding: 0; box-sizing: border-box; }
  html, body { width: 1200px; height: 800px; overflow: hidden; background: var(--paper); }

  .poster {
    position: relative;
    width: 1200px;
    height: 800px;
    overflow: hidden;
    font-family: "League Spartan", "Helvetica Neue", Arial, sans-serif;
    color: var(--ink);
  }

  .forest-backdrop {
    position: absolute;
    inset: 0;
    background:
      radial-gradient(ellipse 520px 380px at 160px 180px, rgba(250,250,250,1) 0%, rgba(250,250,250,0.9) 50%, rgba(250,250,250,0) 100%),
      radial-gradient(ellipse 700px 260px at 620px 120px, rgba(248,248,248,1) 0%, rgba(248,248,248,0) 100%),
      radial-gradient(ellipse 180px 140px at 640px 420px, rgba(122,74,53,0.55) 0%, rgba(122,74,53,0) 100%),
      radial-gradient(ellipse 200px 160px at 1150px 480px, rgba(122,74,53,0.5) 0%, rgba(122,74,53,0) 100%),
      radial-gradient(ellipse 220px 160px at 300px 560px, rgba(110,70,55,0.45) 0%, rgba(110,70,55,0) 100%),
      linear-gradient(180deg, var(--fog) 0%, #ececec 22%, var(--fog-mid) 38%, #6d7768 50%, var(--pine) 64%, #2b3727 80%, var(--pine-deep) 100%);
  }

  .why-block {
    position: absolute;
    left: 40px;
    top: 40px;
    width: 254px;
    height: 348px;
  }

  .why-question {
    position: absolute;
    left: 0;
    top: 348px;
    width: 348px;
    transform: rotate(-90deg);
    transform-origin: top left;
    font-weight: 700;
    font-size: 23px;
    letter-spacing: 1.6px;
    line-height: 24px;
    white-space: nowrap;
    text-transform: uppercase;
  }

  .why-answer {
    position: absolute;
    left: 28px;
    top: 0;
    width: 226px;
    text-transform: uppercase;
  }

  .line {
    display: flex;
    justify-content: space-between;
    align-items: flex-end;
    line-height: 0.78;
    white-space: nowrap;
  }
  .w-900 { font-weight: 900; }
  .w-700 { font-weight: 700; }
  .w-500 { font-weight: 500; }

  .line-feel { font-size: 56px; margin-bottom: 4px; }
  .line-feel .small { font-size: 44px; }
  .line-fulfilled { font-size: 40px; margin-bottom: 6px; }
  .line-fulfilled .small { font-size: 40px; }

  .by-group { display: flex; align-items: stretch; margin-bottom: 6px; }
  .by-mark {
    writing-mode: vertical-rl;
    transform: rotate(180deg);
    font-weight: 900;
    font-size: 22px;
    line-height: 1;
    text-align: center;
    margin-right: 4px;
  }
  .by-lines { flex: 1; display: flex; flex-direction: column; justify-content: space-between; }
  .by-lines .line { font-size: 22px; font-weight: 700; }

  .line-clients, .line-coworkers { font-size: 32px; margin-bottom: 4px; }
  .tiny { font-size: 14px; font-weight: 700; line-height: 1; }
  .line-we { font-size: 50px; margin-bottom: 3px; }
  .line-build { font-size: 38px; margin-bottom: 5px; }
  .line-strong { font-size: 27px; margin-bottom: 5px; }
  .line-impactful { font-size: 38px; margin-bottom: 5px; }
  .line-relationships { font-size: 19px; font-weight: 700; }

  .rally-tag {
    position: absolute;
    left: 42px;
    top: 662px;
    font-family: "Oswald", "Arial Narrow", sans-serif;
    font-size: 38px;
    color: var(--paper);
    letter-spacing: 0.5px;
    line-height: 1;
  }

  .brand-plate {
    position: absolute;
    left: 58px;
    top: 714px;
    width: 234px;
    height: 44px;
    background: var(--paper);
    display: flex;
    align-items: center;
    gap: 8px;
    padding: 0 10px;
  }
  .brand-square { width: 26px; height: 26px; background: var(--brand-blue); flex: none; }
  .brand-name {
    font-weight: 700;
    font-size: 12.5px;
    color: var(--brand-navy);
    text-transform: uppercase;
    letter-spacing: 0.4px;
    line-height: 1.1;
  }
</style>
</head>
<body>
<main class="poster">
  <div class="forest-backdrop" role="img" aria-label="Aerial photograph of a misty pine forest with mist drifting over evergreen and rust-coloured trees"></div>

  <section class="why-block">
    <h1 class="why-question">Why do I come to work?</h1>
    <div class="why-answer">
      <div class="line line-feel"><span class="w-900 small">To</span><span class="w-900">Feel</span></div>
      <div class="line line-fulfilled"><span class="w-900 small">Ful</span><span class="w-700">filled</span></div>
      <div class="by-group">
        <span class="by-mark">By</span>
        <div class="by-lines">
          <div class="line"><span>Empathizing,</span></div>
          <div class="line"><span>Educating &amp;</span></div>
          <div class="line"><span>Empowering</span></div>
        </div>
      </div>
      <div class="line line-clients"><span class="tiny">Our</span><span class="w-900">Clients</span></div>
      <div class="line line-coworkers"><span class="tiny">And</span><span class="w-900">Co-Workers</span></div>
      <div class="line line-we"><span class="tiny">So that</span><span class="w-900">We</span></div>
      <div class="line line-build"><span class="w-900">Can</span><span class="w-700">build</span></div>
      <div class="line line-strong"><span class="w-900">Strong</span><span class="w-700">and</span></div>
      <div class="line line-impactful"><span class="w-900">Impactful</span></div>
      <div class="line line-relationships"><span>Relationships.</span></div>
    </div>
  </section>

  <p class="rally-tag">#OwnTheOutcome</p>

  <div class="brand-plate">
    <span class="brand-square"></span>
    <span class="brand-name">Brindle Cove Property Management</span>
  </div>
</main>
</body>
</html>
```